依頼詳細
「HOT」「あたたか」「着圧」「美脚サポート」をパッケージから感じることができ、ターゲットの女性たちが何気に手に取りたくなるデザインを希望します。
添付資料はあくまでも商品説明書で、パッケージのイメージではありません。
記載項目
サイズ/W9㎝、H15㎝、D3.5㎝ オフセット印刷、ラミネート加工、コート紙
販売什器はお店によって、壁面フックの展開とボックス什器での展開があります
希望イメージ
希望する色
納品ファイル
• イラストレーター形式 (.ai)
補足説明
ご提案はJPGもしくはPDFにてお願いいたします
依頼金額を45900円に変更して、延長しました。
ご提案いただいたランサーの皆様、ありがとうございました。
色々とご提案いただきましたが、暖かいイメージが今少し伝わりにくい気がします。
添付追加資料の指定画像を使って、他社参考パッケージのように「暖かさ」「HOT」のイメージが伝わる着圧ソックスのご提案をお待ちいたします。
■ 選んだ理由

イメージ通りのヴィジュアルをいただきました
度重なる修正にも迅速にご対応いただきまして、ありがとうございました。

■ 提案者全員のお礼・コメント

たくさんのご応募ありがとうございました
良い作品ばかりでとても悩みました。次回からも宜しくお願い申し上げます。

```html
<!DOCTYPE html>
<html lang="ja">
<head>
<meta charset="utf-8">
<title>HOT おやすみ着圧ソックス</title>
<link rel="stylesheet" href="https://fonts.googleapis.com/css2?family=M+PLUS+Rounded+1c:wght@500;800&family=Noto+Sans+JP:wght@400;700;900&display=swap">
<style>
  :root {
    --sky-top: #c9d3ee;
    --sky-mid: #6f86cf;
    --sky-deep: #3d55ad;
    --white: #ffffff;
    --hot-red: #e8382f;
    --title-purple: #b14fc8;
    --title-pink: #e85aa8;
    --tag-pink: #e8408f;
    --star: #f3e23a;
    --ink: #2a2a2a;
    --muted: #444444;
    --disc: #a8a8a8;
    --leg-a: #f2c9a8;
    --leg-b: #e6e0f0;
  }
  html, body { margin: 0; padding: 0; overflow: hidden; }
  body { width: 739px; height: 1200px; background: var(--white); }
  .package {
    position: relative; width: 739px; height: 1200px; overflow: hidden;
    background: linear-gradient(180deg, var(--sky-top) 0%, var(--sky-mid) 40%, var(--sky-deep) 100%);
    font-family: "Noto Sans JP", sans-serif;
  }
  .package__frame {
    position: absolute; inset: 10px; border: 4px solid rgba(255,255,255,0.85);
    border-radius: 18px; pointer-events: none;
  }
  .backdrop { position: absolute; inset: 0; }
  .title { position: absolute; left: 0; top: 0; width: 100%; height: 200px; }
  .title__hot {
    position: absolute; left: 44px; top: 52px; width: 104px; height: 48px;
    background: var(--hot-red); color: var(--white); border-radius: 24px;
    font: 800 38px/48px "M PLUS Rounded 1c", sans-serif; text-align: center;
  }
  .title__night {
    position: absolute; left: 152px; top: 50px; color: var(--white);
    font: 800 40px/50px "M PLUS Rounded 1c", sans-serif; letter-spacing: 1px;
  }
  .title__main {
    position: absolute; left: 392px; top: 34px; color: var(--title-purple);
    font: 900 104px/1 "Noto Sans JP", sans-serif; letter-spacing: 2px;
  }
  .title__sub {
    position: absolute; left: 492px; top: 146px; color: var(--title-pink);
    font: 900 40px/1 "Noto Sans JP", sans-serif; letter-spacing: 2px;
  }
  .product-photo {
    position: absolute; left: 250px; top: 230px; width: 460px; height: 930px;
    background: linear-gradient(160deg, var(--leg-a) 0%, var(--leg-b) 45%, #f4f0f8 100%);
    border-radius: 40% 20% 30% 40% / 20% 10% 20% 20%;
  }
  .tag {
    position: absolute; left: 84px; top: 372px; width: 204px; padding: 12px 0;
    background: var(--tag-pink); color: var(--white); border-radius: 10px;
    transform: rotate(-8deg); text-align: center;
    font: 900 34px/1.2 "Noto Sans JP", sans-serif;
    box-shadow: 0 0 0 4px var(--white);
  }
  .features { position: absolute; left: 70px; top: 555px; }
  .feature { position: relative; height: 116px; }
  .feature__icon {
    position: absolute; left: 0; top: 0; width: 58px; height: 58px;
    background: var(--white); border: 2px solid var(--ink); border-radius: 4px;
  }
  .feature__note { position: absolute; left: 86px; top: 2px; white-space: nowrap; color: var(--muted); font: 400 15px/1 "Noto Sans JP", sans-serif; }
  .feature__name { position: absolute; left: 86px; top: 24px; white-space: nowrap; color: var(--ink); font: 700 24px/1 "Noto Sans JP", sans-serif; }
  .disc { position: absolute; left: 69px; top: 947px; width: 148px; height: 148px; border-radius: 50%; background: var(--disc); }
</style>
</head>
<body>
<main class="package">
  <svg class="backdrop" width="739" height="1200" viewBox="0 0 739 1200" aria-hidden="true">
    <circle cx="650" cy="720" r="440" fill="var(--white)"/>
    <g fill="var(--star)">
      <polygon points="60,150 66,164 81,164 69,173 74,188 60,179 46,188 51,173 39,164 54,164"/>
      <polygon points="335,150 339,160 350,160 341,166 345,177 335,170 325,177 329,166 320,160 331,160"/>
      <polygon points="245,205 249,214 259,214 251,220 254,230 245,224 236,230 239,220 231,214 241,214"/>
      <polygon points="520,270 526,283 540,283 529,291 533,305 520,297 507,305 511,291 500,283 514,283"/>
      <polygon points="32,490 37,502 50,502 40,509 44,522 32,514 20,522 24,509 14,502 27,502"/>
    </g>
  </svg>

  <header class="title">
    <div class="title__hot">HOT</div>
    <div class="title__night">おやすみ</div>
    <h1 class="title__main" style="margin:0">着圧</h1>
    <div class="title__sub">ソックス</div>
  </header>

  <div class="product-photo" role="img" aria-label="着圧ソックスを履いた脚の写真"></div>

  <div class="tag">寝ている間に<br>美脚ケア</div>

  <section class="features">
    <div class="feature">
      <div class="feature__icon" role="img" aria-label="パイル編みのアイコン"></div>
      <div class="feature__note">裏側は暖かで柔らかい</div>
      <div class="feature__name">パイル編み</div>
    </div>
    <div class="feature">
      <div class="feature__icon" role="img" aria-label="着圧効果のアイコン"></div>
      <div class="feature__note">足元を温めながら着圧効果</div>
      <div class="feature__name">寝ながら美脚ケア</div>
    </div>
    <div class="feature">
      <div class="feature__icon" role="img" aria-label="オープントゥソックスのアイコン"></div>
      <div class="feature__note">冬のおやすみ</div>
      <div class="feature__name">オープントゥソックス</div>
    </div>
  </section>

  <div class="disc"></div>
  <div class="package__frame"></div>
</main>
</body>
</html>
```